Personal Brand WordPress Site (Fully functional)

I need a wordpress design for my own personal brand. I am a business strategist and marketing coach, and I provide consulting, speaking, workshops, and coaching programs for entrepreneurs and startups. The website needs to reflect my own personal style and expertise. More information on that below.

My current website is www.velmirgroup.com, but other personal brand websites that I like include:
- www.paulbrenton.com - good example of "as featured in" section and call to action
- www.markhollis.com - sharp site with call to action and him seen as a speaker
- www.ninafarrow.com - check out her speaking section, also good basic style
- www.speakthyplan.com - great video with call to action right up front

Attached are a couple images of me from speaking and working with clients. A full set of images is available at https://files.storvexcloud.net/u/584172/Photos.zip (note that this is a 322 MB file). I'd like to add an element of roll-up-your-sleeves innovation which can be done in supporting images and graphics. Some examples:
- www.kestrow.com - images of sticky notes and whiteboards
- www.leapfieldpartners.com - hand-drawn look to slider images
- www.tableofinvention.com - images on homepage

Target Market(s)

The audience is entrepreneurs, microstartups, and small businesses under 10 employees. However, they will tend to be solopreneurs in service-based businesses like coaches and consultants trying to hit $100k. They also trend female and B2B.

Industry/Entity Type

Marketing

Font styles to use
Serif
Sans Serif
Script

Requirements
Must have
• Homepage much have an "As Seen On" section with logos of Venture Sprint, Kindle Raleton, Novabyte Works, Harbor Town Onward, Collegiate FBLX, and the Millbrook Gazette. The Paul Brenton site above has a good example of one.

There should be testimonial boxes both large and small and with and without image.

There should be a call to action box for people to provide an email address and download an item. For now, you can use placeholder for an ebook or report, and audio file (like a podcast), and a video. Final design will need all 3.

There should be a few blog posts on the homepage and also a Work With Mateo section with Coaching, Consulting, and Training sections.
Nice to have
• Depending on header image design, it may make sense to provide an above-the-menu section with a picture cutout (like Paul Brenton's) and a headline/text/call-to-action button to be seen upon arrival to the site. Scrolling down to menu below will lock menu at the top of the page. This section could be used for temporary promotions or to highlight featured items.
Should not have
• No flowery scripts. If an accent script is used, it should be whiteboard handwriting similar to the Hand of Sean font.

```html
<!DOCTYPE html>
<html lang="en">
<head>
<meta charset="utf-8">
<title>Velmir Co. — Your Marketing Strategy Advisor</title>
<link href="https://fonts.googleapis.com/css2?family=Oswald:wght@300;400;500&family=Open+Sans:wght@300;400;600;700&display=swap" rel="stylesheet">
<style>
:root{
  --ink:#2b2b2b;
  --text:#4a4a4a;
  --muted:#888;
  --rule:#dcdcdc;
  --accent:#f5c400;
  --brand-red:#e0452b;
  --dark:#1d1d1d;
  --white:#fff;
}
*{box-sizing:border-box;margin:0;padding:0}
html,body{width:1200px;height:3315px;overflow:hidden}
body{position:relative;font-family:"Open Sans",Arial,sans-serif;color:var(--text);background:var(--white)}
.abs{position:absolute}
.heading{font-family:"Oswald",Arial,sans-serif;font-weight:300;color:var(--ink);text-align:center;font-size:34px;letter-spacing:.5px}

/* header + hero */
.hero{left:0;top:0;width:1200px;height:690px;overflow:hidden}
.hero-photo{position:absolute;inset:0;background:
  radial-gradient(ellipse 260px 380px at 380px 380px,#4a4036 0%,rgba(40,34,28,.2) 70%,transparent 100%),
  linear-gradient(90deg,#3a332c 0%,#6b5c4a 45%,#8a7a64 70%,#5d5346 100%)}
.topbar{position:absolute;left:0;top:0;width:1200px;height:95px;background:linear-gradient(180deg,rgba(0,0,0,.75),rgba(0,0,0,.35))}
.wordmark{position:absolute;left:140px;top:30px;display:flex;align-items:center;gap:10px;font-family:"Open Sans",sans-serif;font-weight:600;font-size:30px;color:var(--white);white-space:nowrap}
.wordmark b{display:block;width:14px;height:14px;background:var(--white)}
.nav{position:absolute;left:488px;top:50px;display:flex;gap:38px;font-size:14px;color:var(--white);list-style:none;white-space:nowrap}
.social-top{position:absolute;left:955px;top:16px;display:flex;gap:8px}
.social-top i,.follow i{display:block;width:22px;height:22px;border-radius:50%;background:#bfbfbf}
.cta-top{position:absolute;left:858px;top:98px;width:188px;height:28px;background:#1a1a1a;border:1px solid #555;color:var(--white);font-size:11px;font-weight:600;letter-spacing:.5px;text-align:center;line-height:26px}
.hero-title{position:absolute;left:570px;top:245px;font-family:"Oswald",sans-serif;font-weight:300;font-size:60px;line-height:62px;color:var(--white)}
.hero-title em{font-style:normal;color:var(--accent);display:block}
.hero-sub{position:absolute;left:574px;top:383px;font-size:25px;font-weight:600;color:var(--white);white-space:nowrap}
.slider-dots{position:absolute;left:930px;top:666px;width:130px;height:24px;background:var(--white);display:flex;gap:6px;align-items:center;justify-content:center}
.slider-dots i{width:10px;height:10px;border-radius:50%;background:#333}
.slider-dots i.on{background:var(--accent)}

/* seen at */
.seen-title{left:0;top:710px;width:1200px}
.seen-logos{left:200px;top:806px;width:800px;display:flex;justify-content:space-between;align-items:center}
.badge{display:flex;align-items:center;gap:6px;font-family:"Open Sans",sans-serif;font-weight:700;font-size:13px;color:var(--ink);white-space:nowrap}
.badge b{width:14px;height:14px;background:var(--ink);display:block}
.rule{left:0;width:1200px;height:1px;background:var(--rule)}

/* advisor */
.advisor-title{left:0;top:955px;width:1200px;font-size:32px}
.advisor-copy{left:160px;top:1035px;width:880px;font-size:19px;line-height:40px;text-align:center;color:#555}

/* testimonials */
.testimonials{left:0;top:1285px;width:1200px;height:422px;overflow:hidden}
.testi-photo{position:absolute;inset:0;background:radial-gradient(ellipse at 50% 40%,#8f9aa6 0%,#5e6975 55%,#3e4650 100%)}
.testi-shade{position:absolute;inset:0;background:rgba(20,24,30,.35)}
.testi-title{position:absolute;top:32px;width:1200px;text-align:center;font-family:"Oswald",sans-serif;font-weight:300;font-size:32px;color:var(--white)}
.testi-avatar{position:absolute;left:562px;top:93px;width:76px;height:76px;border-radius:50%;background:#2c6fa8;border:3px solid var(--white)}
.testi-quote{position:absolute;left:180px;top:190px;width:840px;text-align:center;color:var(--white);font-size:15px;line-height:26px}
.testi-nav{position:absolute;left:420px;top:305px;width:360px;display:flex;align-items:center;justify-content:center;gap:12px}
.testi-nav i{width:44px;height:44px;border-radius:50%;background:#4e7fa8;border:2px solid var(--white);display:block}
.testi-nav svg{margin:0 8px}

/* downloads */
.dl-title{left:0;top:1732px;width:1200px;font-size:32px}
.dl-sub{left:0;top:1786px;width:1200px;text-align:center;font-size:13px;color:var(--muted)}
.device{height:180px;top:1848px}
.device-caption{top:2050px;font-size:11px;font-weight:600;color:#555;text-align:center;text-transform:uppercase}
.device-caption span{color:var(--accent)}
.view-more{left:555px;top:2128px;width:90px;height:26px;border:1px solid #ccc;border-bottom:2px solid var(--accent);font-size:10px;font-weight:700;text-align:center;line-height:24px;color:#444}

/* work with */
.work{left:0;top:2211px;width:1200px;height:724px;overflow:hidden}
.work-photo{position:absolute;inset:0;background:linear-gradient(135deg,#6f6f6f 0%,#9a9a9a 35%,#7b7b7b 65%,#5a5a5a 100%)}
.work-shade{position:absolute;inset:0;background:rgba(40,40,40,.55)}
.work-title{position:absolute;top:38px;width:1200px;text-align:center;font-family:"Oswald",sans-serif;font-weight:300;font-size:32px;color:var(--white)}
.work-sub{position:absolute;top:88px;width:1200px;text-align:center;font-size:13px;color:#eee}
.spine{position:absolute;left:600px;top:120px;width:2px;height:560px;background:rgba(255,255,255,.7)}
.post{position:absolute;border:1px solid rgba(255,255,255,.55);color:var(--white);padding:16px 18px}
.post h3{font-family:"Oswald",sans-serif;font-weight:300;font-size:20px;margin-bottom:12px}
.post p{font-size:13px;line-height:22px}
.post.left{text-align:right}
.node{position:absolute;left:594px;width:14px;height:14px;border-radius:50%;background:var(--white)}
.arm{position:absolute;height:1px;background:rgba(255,255,255,.7)}

/* footer */
.footer-cta{left:140px;top:3000px;font-family:"Oswald",sans-serif;font-weight:400;font-size:26px;color:var(--ink)}
.footer-note{left:140px;top:3048px;width:340px;font-size:13px;line-height:20px;color:#555;text-align:center}
.email-field{left:140px;top:3126px;width:224px;height:34px;border:1px solid #ccc;font-size:12px;color:#999;padding:8px 10px}
.subscribe{left:372px;top:3126px;width:114px;height:34px;background:var(--accent);font-family:"Oswald",sans-serif;font-size:17px;color:var(--ink);text-align:center;line-height:34px}
.vrule{width:1px;background:var(--rule)}
.f-label{font-size:12px;font-weight:700;color:var(--ink);letter-spacing:.5px}
.f-val{font-size:13px;color:var(--brand-red);line-height:20px}
.f-addr{font-size:13px;color:var(--brand-red);line-height:19px}
.follow{left:862px;top:3150px;display:flex;gap:8px}
.bottom-bar{left:0;top:3265px;width:1200px;height:50px;background:var(--dark);color:var(--accent);font-size:12px;text-align:center;line-height:50px}
</style>
</head>
<body>

<header class="hero abs">
  <div class="hero-photo" role="img" aria-label="Portrait of Mateo in a dark blazer standing in a bright city street, softly blurred"></div>
  <div class="topbar"></div>
  <div class="wordmark"><b></b>Velmir Co.</div>
  <ul class="nav"><li>Home</li><li>About</li><li>Work With Mateo</li><li>Speaking &amp; Workshops</li><li>Clients</li><li>Contact</li></ul>
  <div class="social-top"><i></i><i></i><i></i><i></i></div>
  <div class="cta-top">GET IN TOUCH FOR DETAILS</div>
  <h1 class="hero-title">Build<em>a Better Business</em></h1>
  <p class="hero-sub">simply dummy text of the printing and typesetting</p>
  <div class="slider-dots"><i class="on"></i><i></i><i></i><i></i><i></i><i></i></div>
</header>

<h2 class="heading abs seen-title">You May Have Seen Me At</h2>
<div class="seen-logos abs">
  <div class="badge"><b></b>Venture Sprint</div>
  <div class="badge"><b></b>Kindle Raleton</div>
  <div class="badge"><b></b>Novabyte Works</div>
  <div class="badge"><b></b>Harbor Town Onward</div>
  <div class="badge"><b></b>Collegiate FBLX</div>
  <div class="badge"><b></b>Millbrook Gazette</div>
</div>
<div class="rule abs" style="top:895px"></div>

<h2 class="heading abs advisor-title">Your Marketing Strategy Advisor</h2>
<p class="advisor-copy abs">We enable sales by crafting marketing messages that matter to your customers. We help you better understand your customer, craft an effective value proposition, develop an authentic brand story, and then have an engaging sales conversation. The alignment of your marketing message with your sales approach means more deals, a faster sales cycle, and increased customer retention.</p>

<section class="testimonials abs">
  <div class="testi-photo" role="img" aria-label="Blurred photo of an audience at a workshop"></div>
  <div class="testi-shade"></div>
  <h2 class="testi-title">Testimonials</h2>
  <div class="testi-avatar" role="img" aria-label="Client portrait"></div>
  <p class="testi-quote">I have only spent 20 minutes with Mateo to be impressed. Mateo is a thinker and a good one too. He understands the importance of strategy when working on any initiative and takes the time to see a project from a 360 degree viewpoint.</p>
  <div class="testi-nav">
    <svg width="12" height="18" viewBox="0 0 12 18"><path d="M10 2 3 9l7 7" stroke="#fff" stroke-width="2.5" fill="none"/></svg>
    <i></i><i></i><i></i><i></i><i></i>
    <svg width="12" height="18" viewBox="0 0 12 18"><path d="M2 2l7 7-7 7" stroke="#fff" stroke-width="2.5" fill="none"/></svg>
  </div>
</section>

<h2 class="heading abs dl-title">Download Audio - Video</h2>
<p class="dl-sub abs">(Coaching, Consulting, and Training sections)</p>
<div class="device abs" style="left:140px;width:250px;background:linear-gradient(180deg,#2a2e38,#5a6070)" role="img" aria-label="Laptop showing a video player"></div>
<div class="device abs" style="left:470px;width:260px;background:linear-gradient(180deg,#dfe6ee,#9fb2c6)" role="img" aria-label="Monitor, tablet and phone showing an audio download page"></div>
<div class="device abs" style="left:810px;width:250px;background:linear-gradient(180deg,#1c4f8a,#b8242a)" role="img" aria-label="Laptop showing a report cover"></div>
<p class="device-caption abs" style="left:140px;width:250px">Simply dummy text <span>›</span></p>
<p class="device-caption abs" style="left:460px;width:280px;line-height:16px">Lorem Ipsum has been the industry's standard dummy text <span>›</span></p>
<p class="device-caption abs" style="left:810px;width:250px">Standard dummy text <span>›</span></p>
<div class="view-more abs">VIEW MORE</div>
<div class="rule abs" style="top:2206px"></div>

<section class="work abs">
  <div class="work-photo" role="img" aria-label="Wall of sticky notes and client logos on a whiteboard"></div>
  <div class="work-shade"></div>
  <h2 class="work-title">Work With Mateo</h2>
  <p class="work-sub">(Recent Posts)</p>
  <div class="spine"></div>

  <div class="post left" style="left:150px;top:150px;width:400px;height:210px">
    <h3>Our Approach</h3>
    <p>Many companies experience a disconnect between their marketing strategy and sales activity. The high level company message is often hidden in sales collateral, which the National Sales Council estimates 80 - 90% is never read, or it stays after slide.</p>
  </div>
  <div class="arm" style="left:550px;top:176px;width:50px"></div>
  <div class="node" style="top:169px"></div>

  <div class="post left" style="left:150px;top:378px;width:400px;height:130px">
    <h3>Archives</h3>
    <p>January 2014<br>April 2014<br>May 2014</p>
  </div>
  <div class="arm" style="left:550px;top:400px;width:50px"></div>
  <div class="node" style="top:393px"></div>

  <div class="post left" style="left:150px;top:528px;width:400px;height:135px">
    <h3>Categories</h3>
    <p>Lorem Ipsum<br>text of the printing and typesetting<br>dummy text ever since the 1500s</p>
  </div>
  <div class="arm" style="left:550px;top:552px;width:50px"></div>
  <div class="node" style="top:545px"></div>

  <div class="post" style="left:650px;top:150px;width:400px;height:135px">
    <h3>1. Client Insights</h3>
    <p>Taking the time to understand your client's needs and motivations for buying helps lay the foundation for effective value messaging.</p>
  </div>
  <div class="arm" style="left:608px;top:176px;width:42px"></div>

  <div class="post" style="left:650px;top:312px;width:400px;height:135px">
    <h3>2. Message Strategy</h3>
    <p>Insights gained from our client conversations are then used to craft language that supports your value and engages the prospect.</p>
  </div>
  <div class="arm" style="left:608px;top:336px;width:42px"></div>
  <div class="node" style="top:329px"></div>

  <div class="post" style="left:650px;top:474px;width:400px;height:135px">
    <h3>3. Sales Conversation</h3>
    <p>Tools and techniques to engage clients in a conversation rather than a sales pitch allow you to implement your business development strategy.</p>
  </div>
  <div class="arm" style="left:608px;top:496px;width:42px"></div>
  <div class="node" style="top:489px"></div>
</section>

<footer>
  <h2 class="footer-cta abs">LIKE WHAT WE HAVE TO SAY?</h2>
  <p class="footer-note abs">"Put your email in that box, press subscribe, and we'll give you some ideas and inspiration."</p>
  <div class="email-field abs">Enter email here...</div>
  <div class="subscribe abs">SUBSCRIBE</div>

  <div class="vrule abs" style="left:600px;top:2990px;height:220px"></div>
  <div class="vrule abs" style="left:845px;top:2990px;height:220px"></div>

  <div class="abs" style="left:630px;top:2998px">
    <p class="f-label">E-MAIL US</p><p class="f-val">info@velmirgroup.com</p>
    <p class="f-label" style="margin-top:22px">CALL US NOW!</p><p class="f-val">123.123.1234</p>
    <p class="f-label" style="margin-top:22px">SKYPE</p><p class="f-val" style="color:var(--text)">velmirco</p>
  </div>
  <div class="abs" style="left:862px;top:2998px">
    <p class="f-label">CONTACT</p>
    <p class="f-addr">418 Linden Ave.<br>Loft 214<br>Raleton, NC 28419</p>
    <p class="f-label" style="margin-top:22px">FOLLOW US</p>
  </div>
  <div class="follow abs"><i></i><i></i><i></i><i></i></div>

  <div class="bottom-bar abs">© 2014 The Velmir Company LLC</div>
</footer>

</body>
</html>
```